Real Estate Development requires a tri-fold corporate brochure

I need a clean, elegant, Corporate tri-fold brochure for a real estate development. Currently operation in Dubai, we plan to enter European markets and will hand out the brochures to potential, future cooperation partners. A color combination in line with our logo would be great. The overall design should communicate that we are holding numerous high-end properties in Dubai and London and our financial strength.

Target Market(s)

Europe

Industry/Entity Type

Real Estate Development

Contact Information for Business Card

Lorin Haswell, MBA
Senior Business Development Manager
Pinecrest Holdings UAE
Cell UAE: +971 52 487 3916
Cell Austria: +43 664 318 2097
loha@pinecrestholdings.ae

Requirements
Must have
• Clean, corporate design, not too colorful, a few nice pictures of existing real estate properties. See the attached pdf-document for more details.
Nice to have
• Refurbished logo

```html
<!DOCTYPE html>
<html lang="en">
<head>
<meta charset="utf-8">
<title>Pinecrest Holdings – Tri-fold Brochure and Business Card</title>
<link rel="stylesheet" href="https://fonts.googleapis.com/css2?family=Josefin+Sans:wght@300;400;600&display=swap">
<style>
  :root {
    --green: #a3c93a;
    --green-dark: #8db52b;
    --white: #ffffff;
    --ink: #4a4a4a;
    --ink-soft: #6b6b6b;
    --page: #ffffff;
    --font: "Josefin Sans", Arial, sans-serif;
  }
  html, body { margin: 0; padding: 0; overflow: hidden; background: var(--page); }
  .canvas { position: relative; width: 781px; height: 1200px; overflow: hidden; font-family: var(--font); color: var(--ink); }
  .abs { position: absolute; }
  .photo { position: absolute; }
  .sheet { position: absolute; box-shadow: 0 1px 4px rgba(0,0,0,.25); }

  /* Outside spread */
  .outside { left: 68px; top: 44px; width: 636px; height: 426px; background: var(--green); }
  .panel-welcome { left: 2px; top: 200px; width: 200px; height: 218px; background: var(--white); }
  .welcome-title { margin: 14px 0 0 30px; color: var(--green); font-weight: 300; font-size: 13px; line-height: 14px; text-transform: uppercase; }
  .body-copy { font-size: 4.6px; line-height: 6.4px; color: var(--ink-soft); margin: 7px 14px 0 30px; }
  .body-copy p { margin: 0 0 5px; }

  .brand { color: var(--white); font-weight: 600; font-size: 13px; display: flex; align-items: center; gap: 5px; white-space: nowrap; }
  .brand .mark { width: 8px; height: 8px; background: var(--white); flex: none; }
  .brand.dark { color: var(--ink); }
  .brand.dark .mark { background: var(--green); }

  .cover-contact { left: 202px; width: 202px; text-align: center; color: var(--white); font-size: 7.5px; line-height: 15px; font-weight: 300; }
  .contact-line { display: flex; align-items: center; justify-content: center; gap: 4px; }
  .contact-line svg { width: 9px; height: 9px; flex: none; }
  .web { color: var(--white); font-weight: 600; font-size: 10.5px; }

  .panel-cover { left: 404px; top: 0; width: 232px; height: 418px; background: var(--white); overflow: hidden; }
  .cover-tagline { left: 0; top: 370px; width: 232px; text-align: center; font-size: 8px; line-height: 10px; color: var(--ink); text-transform: uppercase; }

  /* Inside spread */
  .inside { left: 68px; top: 484px; width: 636px; height: 427px; background: var(--white); }
  .strip { left: 0; width: 636px; height: 11px; background: var(--green); }
  .heading-band { left: 0; top: 156px; width: 636px; height: 35px; background: var(--green); }
  .col-head { top: 168px; color: var(--white); font-size: 11.5px; line-height: 12px; text-transform: uppercase; letter-spacing: .3px; font-weight: 400; }
  .col { top: 200px; font-size: 4.4px; line-height: 6.2px; color: var(--ink-soft); }
  .col p { margin: 0 0 4px; }
  .sub-head { color: var(--green); font-size: 6px; text-transform: uppercase; margin: 3px 0 3px; }
  .bullets { list-style: none; margin: 0 0 4px; padding: 0; }
  .bullets li { position: relative; padding-left: 6px; margin-bottom: 3px; }
  .bullets li::before { content: ""; position: absolute; left: 0; top: 1px; width: 3px; height: 3px; background: var(--green); }
  .bullets.wide li { margin-bottom: 6.1px; }

  /* Business card */
  .card-front { left: 100px; top: 937px; width: 263px; height: 155px; background: var(--white); overflow: hidden; }
  .card-band { left: 0; bottom: 0; width: 263px; height: 26px; background: var(--green); color: var(--white); font-size: 8px; text-align: center; line-height: 27px; text-transform: uppercase; }
  .card-back { left: 390px; top: 937px; width: 253px; height: 155px; background: var(--green); overflow: hidden; }
  .card-foot { left: 0; bottom: 0; width: 253px; height: 24px; background: var(--white); }
  .card-name { left: 82px; top: 24px; color: var(--white); font-size: 10px; line-height: 11px; text-transform: uppercase; border-bottom: 1px solid var(--white); padding-bottom: 3px; width: 140px; }
  .card-role { left: 82px; top: 43px; color: var(--white); font-size: 6px; line-height: 7px; font-weight: 300; }
  .card-lines { left: 82px; top: 56px; color: var(--white); font-size: 7px; line-height: 13.5px; font-weight: 300; }
  .card-lines .contact-line { justify-content: flex-start; }
  .card-web { right: 8px; bottom: 7px; color: var(--green-dark); font-weight: 600; font-size: 8.5px; }
</style>
</head>
<body>
<main class="canvas">

  <!-- Outside spread -->
  <section class="sheet outside">
    <div class="photo" style="left:2px;top:8px;width:200px;height:180px;background:linear-gradient(180deg,#1c2a4a 0%,#3a3550 45%,#b8742e 80%,#6e4a2a 100%);" role="img" aria-label="Photo of a city skyline at dusk with lit towers along the waterfront"></div>
    <div class="abs panel-welcome">
      <h2 class="welcome-title">Welcome<br>to Pinecrest Holdings</h2>
      <div class="body-copy">
        <p>Pinecrest Holdings is a UAE based diversified real estate investment and development company started in 2009, primarily focused on private equity and real estate, and over the years pioneered also in the field of asset and property management.</p>
        <p>With our strong interest free financial back ground with an essential combination of local and international expertise which is fully adherence from commitment to transparency, we are successful at its inception, to capitalized on profitable market niches by acquiring, developing and managing investment grade commercial real estate properties in United Arab Emirates, Central Asia and Europe.</p>
        <p>Pinecrest Holdings is confident to achieve the highest standards in developing exceptional investment opportunities and shall be the first preference of our clients both at national and internationally.</p>
      </div>
    </div>

    <div class="abs brand" style="left:235px;top:290px;">Pinecrest Holdings LTD<span class="mark"></span></div>
    <div class="abs cover-contact" style="top:320px;">
      <div>Office 714, Marlow Tower JLT Dubai, UAE</div>
      <div class="contact-line">
        <svg viewBox="0 0 10 10"><circle cx="5" cy="5" r="4.5" fill="none" stroke="#fff" stroke-width=".8"/><path d="M3.4 2.8l1 .9-.5.8a3.5 3.5 0 0 0 1.6 1.6l.8-.5.9 1-.7.8C5 7.3 2.8 5.1 2.6 3.5z" fill="#fff"/></svg>
        <span>+971 4 268 1137</span>
      </div>
      <div class="contact-line">
        <svg viewBox="0 0 10 10"><circle cx="5" cy="5" r="4.5" fill="none" stroke="#fff" stroke-width=".8"/><rect x="2.6" y="3.4" width="4.8" height="3.3" fill="none" stroke="#fff" stroke-width=".6"/><path d="M2.6 3.4L5 5.3l2.4-1.9" fill="none" stroke="#fff" stroke-width=".6"/></svg>
        <span>info@pinecrestholdings.ae</span>
      </div>
      <div class="web" style="margin-top:14px;">www.pinecrestholdings.ae</div>
    </div>

    <div class="abs panel-cover">
      <div class="photo" style="left:0;top:0;width:232px;height:300px;background:linear-gradient(180deg,#202e56 0%,#3d3b66 40%,#a0653a 75%,#4a3a32 100%);" role="img" aria-label="Photo of illuminated skyscrapers at night"></div>
      <div class="abs" style="left:0;top:286px;width:232px;height:14px;background:var(--green);"></div>
      <div class="abs brand dark" style="left:34px;top:338px;">Pinecrest Holdings LTD<span class="mark"></span></div>
      <div class="abs" style="left:34px;top:356px;width:164px;height:2px;background:var(--green);"></div>
      <div class="abs cover-tagline">Real estate investment<br>and development</div>
    </div>
  </section>

  <!-- Inside spread -->
  <section class="sheet inside">
    <div class="abs strip" style="top:0;"></div>
    <div class="photo" style="left:2px;top:11px;width:201px;height:145px;background:linear-gradient(180deg,#6fa6c8 0%,#c9b79a 45%,#a8946f 100%);" role="img" aria-label="Photo of tall residential towers beside the sea"></div>
    <div class="photo" style="left:203px;top:11px;width:201px;height:145px;background:linear-gradient(180deg,#cfe0ee 0%,#d9c39a 40%,#8a9e5a 75%,#5f8d3a 100%);" role="img" aria-label="Photo of a villa with a landscaped front garden"></div>
    <div class="photo" style="left:404px;top:11px;width:230px;height:145px;background:linear-gradient(180deg,#e6edf3 0%,#9fb4c8 50%,#6c8194 85%,#7a8a6a 100%);" role="img" aria-label="Photo of a modern high-rise skyline under a pale sky"></div>
    <div class="abs heading-band"></div>
    <h3 class="abs col-head" style="left:32px;margin:0;">Investment</h3>
    <h3 class="abs col-head" style="left:221px;margin:0;">Property Management</h3>
    <h3 class="abs col-head" style="left:430px;margin:0;">Development</h3>

    <div class="abs col" style="left:32px;width:160px;">
      <p>Pinecrest Holdings provides end-to-end property investment services to investors around the world and specially in Dubai Market.</p>
      <p>From initial analysis, advice, financing and process support through to ongoing management and, ultimately, the perfectly timed achievement of returns, we are the trusted partner you need to seamlessly guide you through the complex world of international property investment.</p>
      <div class="sub-head">Invest with us</div>
      <p>Every investor is different, with a unique investment strategy, risk profile and market interest. We are confident we can make property investment work better for you than any other firm operating in our markets.</p>
      <p>Our clients who are interested in investing abroad trust us to offer considered, expert investment advice and provide access to high-quality investment opportunities.</p>
      <p>Over the years, we've become highly proficient in unlocking the investment potential within the world's real estate markets.</p>
      <p>We help our clients make the potential of investing in properties a successful part of their personal wealth strategies.</p>
    </div>

    <div class="abs col" style="left:221px;width:168px;">
      <p>We manage your property and help you save money. We manage the leasing, maintenance, rent collection, all activity related to your property needs.</p>
      <p>Valuation: Independent and accurate valuations are fundamental to the property market. Thus whilst studying the economic and social trend, the forces of demand and supply, and the ease of transferability we are able to accurately value your property.</p>
      <ul class="bullets">
        <li>Leasing (Local | International)</li>
        <li>Sales (Local | International)</li>
      </ul>
      <p>We make sure to offer you all services what is listed here.</p>
      <ul class="bullets">
        <li>Evaluate the property and determine an accurate rental rate</li>
        <li>Market the property for rent</li>
        <li>Tenant Screening and Selection</li>
        <li>Rent collection</li>
        <li>Evictions Legal Inspections Financial</li>
        <li>Maintenance, Repairs, and Remodeling</li>
        <li>Tenant Move In/Tenant Move Out</li>
        <li>Put the property back on the market for rent</li>
      </ul>
      <p>At this point you may be thinking, "Ok, so that's what what they can do, but how does all of this benefit me and relate to the big picture of my real estate investment strategy?". Please Contact us to find out.</p>
    </div>

    <div class="abs col" style="left:430px;width:140px;">
      <p>We have access to an exceptional client base of long-term property investors looking for high-quality opportunities in Dubai real estate.</p>
      <p>These investors trust us to do the hard work for them, to source and deliver well-researched, reliable investments.</p>
      <p>Range of services in the field of Property Development consists primarily of the following:</p>
      <ul class="bullets wide" style="margin-top:6px;">
        <li>Strategic advice</li>
        <li>Studies of potential</li>
        <li>Market analyses</li>
        <li>Cost assessments</li>
        <li>Profitability assessments</li>
        <li>Land development</li>
        <li>Planning case management</li>
        <li>Property law advice</li>
        <li>Property creation</li>
        <li>Risk and Security</li>
      </ul>
    </div>
    <div class="photo" style="left:510px;top:283px;width:124px;height:116px;background:linear-gradient(180deg,#9cc0dc 0%,#c8d3dc 45%,#7f8c96 100%);" role="img" aria-label="Photo of a glass office tower beside a waterway"></div>
    <div class="abs strip" style="top:416px;"></div>
  </section>

  <!-- Business card front -->
  <section class="sheet card-front">
    <div class="abs brand dark" style="left:42px;top:62px;font-size:14px;">Pinecrest Holdings LTD<span class="mark"></span></div>
    <div class="abs" style="left:0;top:113px;width:263px;height:5px;background:var(--green);"></div>
    <div class="abs card-band">Real estate investment and development</div>
  </section>

  <!-- Business card back -->
  <section class="sheet card-back">
    <div class="abs card-foot"></div>
    <div class="abs card-name">Lorin Haswell, MBA</div>
    <div class="abs card-role">Senior Business Development Manager</div>
    <div class="abs card-lines">
      <div>Pinecrest Holdings UAE</div>
      <div class="contact-line">
        <svg viewBox="0 0 10 10"><circle cx="5" cy="5" r="4.5" fill="none" stroke="#fff" stroke-width=".8"/><path d="M3.4 2.8l1 .9-.5.8a3.5 3.5 0 0 0 1.6 1.6l.8-.5.9 1-.7.8C5 7.3 2.8 5.1 2.6 3.5z" fill="#fff"/></svg>
        <span>Cell UAE: +971 52 487 3916</span>
      </div>
      <div class="contact-line">
        <svg viewBox="0 0 10 10"><circle cx="5" cy="5" r="4.5" fill="none" stroke="#fff" stroke-width=".8"/><path d="M3.4 2.8l1 .9-.5.8a3.5 3.5 0 0 0 1.6 1.6l.8-.5.9 1-.7.8C5 7.3 2.8 5.1 2.6 3.5z" fill="#fff"/></svg>
        <span>Cell Austria: +43 664 318 2097</span>
      </div>
      <div class="contact-line">
        <svg viewBox="0 0 10 10"><circle cx="5" cy="5" r="4.5" fill="none" stroke="#fff" stroke-width=".8"/><rect x="2.6" y="3.4" width="4.8" height="3.3" fill="none" stroke="#fff" stroke-width=".6"/><path d="M2.6 3.4L5 5.3l2.4-1.9" fill="none" stroke="#fff" stroke-width=".6"/></svg>
        <span>loha@pinecrestholdings.ae</span>
      </div>
    </div>
    <div class="abs card-web">www.pinecrestholdings.ae</div>
  </section>

</main>
</body>
</html>
```